Plakat-Design Workshop gegen Prüfungsangst
Zielgruppe
Prüfungsangst überwinden mittels Workshops: 'Selbsthypnose erlernen'
Zielgruppe Studenten
Schweißausbrüche, Blackout, und Resignation.
Viele kennen diese unangenehmen Momente, wenn eine Prüfung begonnen hat und die Aufgabenstellungen scheinbar unlösbar sind.
Dann ist Entspannung nahezu unmöglich. Das Stresshormon Cortisol wurde bereits ausgeschüttet. Es beeinträchtigt die Erinnerung an das Gelernte.
Die mentale Vorbereitung sollte schon viel eher ansetzen, wenn es noch nicht zu spät ist. Wenn der Körper noch nicht verkrampft ist.
Selbsthypnose vor Prüfungen ist hier eine tolle Möglichkeit.
Mit Hilfe einer geführten Selbsthypnoseanleitung ist es Dir möglich Dein Unterbewusstsein so zu programmieren, dass diese Übererregungszustände vor Prüfungssituationen deutlich reduziert werden.
Aufgabenstellung
DINA 4 Plakat, 'Prüfungsangst?' mit einem Freifeld, wo man Ort, Datum und Zeit der Veranstaltung 'Selbsthypnose erlernen'
(Selbstsicher in die Prüfung) eindrucken kann.
darunter:
Anmeldung: Tel: 01563 8274015
Dipl. Sportl. Henrik Malow Mentaltraining
weitere Infos auch über Einzelsitzungen: www.malow-trance.de

```html
<!DOCTYPE html>
<html lang="de">
<head>
<meta charset="utf-8">
<title>Prüfungsangst? – Workshop Selbsthypnose erlernen</title>
<link href="https://fonts.googleapis.com/css2?family=Sarabun:wght@400;600;700&display=swap" rel="stylesheet">
<style>
  :root {
    --red: #e22d24;
    --ink: #111111;
    --muted: #8a8a8a;
    --paper: #ffffff;
    --photo-warm-1: #b7763e;
    --photo-warm-2: #8a5a30;
    --photo-blue: #9fb2cc;
    --portrait-1: #b9b9b6;
    --portrait-2: #7d8797;
    --seal-ring: #c9d3d8;
    --seal-core: #1a7f96;
  }
  * { margin: 0; padding: 0; box-sizing: border-box; }
  html, body { width: 866px; height: 1200px; overflow: hidden; background: var(--paper); }
  body { font-family: "Sarabun", sans-serif; color: var(--ink); }

  .poster { position: relative; width: 866px; height: 1200px; background: var(--paper); overflow: hidden; }

  .hero-photo {
    position: absolute; left: 0; top: 0; width: 866px; height: 381px;
    background: linear-gradient(100deg, var(--photo-warm-1) 0%, var(--photo-warm-2) 45%, #a07f6a 70%, var(--photo-blue) 100%);
  }
  .hero-rule { position: absolute; left: 0; top: 388px; width: 866px; height: 5px; background: var(--red); }

  .headline {
    position: absolute; left: 27px; top: 404px;
    font-size: 121px; font-weight: 600; line-height: 1; color: var(--red);
    letter-spacing: -0.5px; white-space: nowrap;
  }
  .symptoms {
    position: absolute; left: 31px; top: 543px;
    font-size: 38px; font-weight: 700; line-height: 1.1; white-space: nowrap;
  }
  .intro {
    position: absolute; left: 31px; top: 600px;
    font-size: 27px; font-weight: 400; line-height: 35.8px; white-space: nowrap;
  }
  .claim {
    position: absolute; left: 29px; top: 736px;
    font-size: 66px; font-weight: 600; line-height: 1; color: var(--red);
    letter-spacing: -0.5px; white-space: nowrap;
  }

  .portrait-photo {
    position: absolute; left: 32px; top: 826px; width: 242px; height: 324px;
    background: linear-gradient(180deg, var(--portrait-1) 0%, #a4a7ab 45%, var(--portrait-2) 100%);
  }

  .seal { position: absolute; left: 217px; top: 1025px; width: 164px; height: 164px; }

  .workshop { position: absolute; left: 400px; top: 822px; width: 436px; }
  .workshop-title { font-size: 24px; font-weight: 700; line-height: 29px; }
  .event-field { margin-top: 10px; }
  .event-row { display: flex; align-items: flex-end; height: 38px; font-size: 22px; }
  .event-label { width: 78px; }
  .event-blank { flex: 1; border-bottom: 1px solid var(--muted); height: 28px; }

  .contact { position: absolute; left: 400px; top: 1012px; font-size: 22px; line-height: 28px; white-space: nowrap; }
  .contact-title, .contact-web { font-weight: 700; }

  .foot-band { position: absolute; left: 0; top: 1161px; width: 866px; height: 39px; background: var(--red); }
</style>
</head>
<body>
  <main class="poster">
    <div class="hero-photo" role="img" aria-label="Foto: Studierende in einer Prüfung, vorne eine junge Frau, die sich besorgt an den Kopf fasst"></div>
    <div class="hero-rule"></div>

    <h1 class="headline">Prüfungsangst?</h1>
    <p class="symptoms">Schweißausbrüche, Blackout &amp; Resignation?</p>
    <p class="intro">Im Workshop lernst Du mit einer geführten Selbsthypnose, Dein<br>Unterbewusstsein so zu programmieren, dass Übererregung vor<br>Prüfungssituationen deutlich reduziert wird.</p>

    <h2 class="claim">Selbstsicher in die Prüfung!</h2>

    <div class="portrait-photo" role="img" aria-label="Porträtfoto des Mentaltrainers vor einer Betonwand"></div>

    <section class="workshop">
      <p class="workshop-title">Workshop: Selbsthypnose erlernen</p>
      <div class="event-field">
        <div class="event-row"><span class="event-label">Ort:</span><span class="event-blank"></span></div>
        <div class="event-row"><span class="event-label">Datum:</span><span class="event-blank"></span></div>
        <div class="event-row"><span class="event-label">Zeit:</span><span class="event-blank"></span></div>
      </div>
    </section>

    <div class="foot-band"></div>

    <svg class="seal" viewBox="0 0 164 164" aria-hidden="true">
      <circle cx="82" cy="82" r="82" fill="#ffffff"/>
      <circle cx="82" cy="82" r="72" fill="var(--seal-ring)" stroke="var(--seal-core)" stroke-width="2"/>
      <circle cx="82" cy="82" r="48" fill="#e8eef0"/>
      <circle cx="82" cy="82" r="36" fill="var(--seal-core)"/>
    </svg>

    <div class="contact">
      <p class="contact-title">Anmeldung:</p>
      <p>Tel: 01563 8274015</p>
      <p>Dipl. Sportl. Henrik Malow Mentaltraining</p>
      <p>weitere Infos auch über Einzelsitzungen:</p>
      <p class="contact-web">www.malow-trance.de</p>
    </div>
  </main>
</body>
</html>
```